Business Card for a mobile physiotherapy company

I need a layout for a business card for a mobile physiotherapy company.
Slogan is "Mobile Physiotherapy - Your Road To Recovery"
Phone number is 867-402-5913
Email VantrePhysio@mailbright.ca (subject to change with website)
Website www.VantrePhysio.ca
My name and credentials: Kent Vantre Kent Vantre, BSc(kin), MPT, CAFCI, IMS
Information maybe included: Direct Billing, Services including Physiotherapy, IMS, acupuncture
Maybe include facebook and instagram logos
One side with the logo clean and sharp
Other side with details, try not to look too busy, keep everything concise

```html
<!DOCTYPE html>
<html lang="en">
<head>
<meta charset="utf-8">
<title>Vantre Physio – Business Card</title>
<link rel="stylesheet" href="https://fonts.googleapis.com/css2?family=Roboto:ital,wght@0,400;0,500;0,700;1,400&display=swap">
<style>
  :root {
    --navy: #2c4a72;
    --green: #175c4a;
    --paper: #f1f1f1;
    --ground: #8c8c8c;
    --slogan: #5e5e5e;
    --white: #ffffff;
  }
  * { margin: 0; padding: 0; box-sizing: border-box; }
  html, body { width: 1125px; height: 1200px; overflow: hidden; }
  body {
    background: var(--ground);
    font-family: "Roboto", Arial, sans-serif;
    position: relative;
  }
  .card {
    position: absolute;
    left: 151px;
    width: 826px;
    height: 471px;
    background: var(--paper);
    overflow: hidden;
  }
  .card--front { top: 106px; }
  .card--back { top: 639px; }

  /* Front */
  .details-panel {
    position: absolute; left: 0; top: 0;
    width: 384px; height: 100%;
    background: var(--navy);
    color: var(--white);
    padding: 128px 0 0 55px;
  }
  .holder-name { font-size: 30px; font-weight: 700; line-height: 1; letter-spacing: .2px; }
  .holder-credentials { font-size: 19px; font-weight: 500; margin-top: 4px; }
  .holder-note { font-size: 20px; font-weight: 500; margin-top: 4px; }
  .contact-list { list-style: none; margin-top: 82px; }
  .contact-item {
    display: flex; align-items: center; gap: 11px;
    font-size: 19.5px; line-height: 27px;
  }
  .contact-icon { width: 18px; height: 18px; flex: none; }

  .brand-block {
    position: absolute; left: 384px; right: 0; top: 0; bottom: 0;
    display: flex; flex-direction: column; align-items: center; justify-content: center;
    padding-top: 40px;
  }
  .brand-name {
    color: var(--navy);
    font-weight: 700;
    font-size: 40px;
    letter-spacing: 6px;
    text-align: center;
    line-height: 1.15;
  }

  /* Back */
  .social-handle {
    position: absolute; right: 46px; top: 42px;
    display: flex; align-items: center; gap: 8px;
    color: var(--navy); font-size: 18px; font-weight: 500;
  }
  .social-dot { width: 30px; height: 30px; border-radius: 50%; background: var(--navy); }
  .back-brand {
    position: absolute; left: 0; right: 0; top: 160px;
    text-align: center;
    color: var(--navy);
    font-weight: 700;
    font-size: 62px;
    letter-spacing: 9px;
  }
  .slogan {
    position: absolute; left: 0; right: 0; top: 392px;
    text-align: center;
    font-style: italic;
    font-size: 20px;
    color: var(--slogan);
  }
  .services {
    position: absolute; left: 0; right: 0; top: 421px;
    text-align: center;
    font-size: 20px;
    color: var(--green);
  }
</style>
</head>
<body>
  <section class="card card--front">
    <div class="details-panel">
      <h1 class="holder-name">KENT VANTRE</h1>
      <p class="holder-credentials">BSc(kin), MPT, CAFCI, IMS</p>
      <p class="holder-note">Direct Billing</p>
      <ul class="contact-list">
        <li class="contact-item">
          <svg class="contact-icon" viewBox="0 0 24 24"><path fill="#fff" d="M6.6 10.8a15 15 0 0 0 6.6 6.6l2.2-2.2c.3-.3.7-.4 1-.2 1.1.4 2.3.6 3.6.6.6 0 1 .4 1 1V20c0 .6-.4 1-1 1A17 17 0 0 1 3 4c0-.6.4-1 1-1h3.5c.6 0 1 .4 1 1 0 1.3.2 2.5.6 3.6.1.3 0 .7-.2 1z"/></svg>
          <span>867-402-5913</span>
        </li>
        <li class="contact-item">
          <svg class="contact-icon" viewBox="0 0 24 24"><path fill="#fff" d="M3 6h18v12H3z"/><path fill="none" stroke="#2c4a72" stroke-width="1.8" d="M3.5 6.5 12 13l8.5-6.5"/></svg>
          <span>VantrePhysio@mailbright.ca</span>
        </li>
        <li class="contact-item">
          <svg class="contact-icon" viewBox="0 0 24 24"><circle cx="12" cy="12" r="10" fill="#fff"/><path fill="none" stroke="#2c4a72" stroke-width="1.5" d="M2 12h20M12 2c3 3 3 17 0 20M12 2c-3 3-3 17 0 20"/></svg>
          <span>www.VantrePhysio.ca</span>
        </li>
      </ul>
    </div>
    <div class="brand-block">
      <p class="brand-name">VANTRE<br>PHYSIO</p>
    </div>
  </section>

  <section class="card card--back">
    <div class="social-handle"><span class="social-dot"></span><span>@VantrePhysio</span></div>
    <p class="back-brand">VANTRE PHYSIO</p>
    <p class="slogan">Mobile Physiotherapy - Your Road To Recovery</p>
    <p class="services">Physiotherapy • IMS • Acupuncture</p>
  </section>
</body>
</html>
```